PebbleLoom screens tidy up

We would like advice on how to better present the following home page and overview pages.

The existing website is functional, but the pages don't appear professionals and pleasing to the eye. We would specifically like feedback on alignment and padding of icons and text to make the screen more appealing and polished.

We are following the willow design system.

1 page

Sans Serif
• IBM Plex, Poppins

```html
<!DOCTYPE html>
<html lang="en">
<head>
<meta charset="utf-8">
<title>PebbleLoom – Home</title>
<link rel="stylesheet" href="https://fonts.googleapis.com/css2?family=Lato:wght@400;700&display=swap">
<style>
:root{
  --topbar:#434343;
  --page:#f4f4f6;
  --panel:#ffffff;
  --text:#161616;
  --muted:#8a8a8a;
  --line:#e0e0e0;
  --accent:#0f62fe;
  --brand:#f1a33a;
  --nav-active:#e8e8e8;
  --illus:#d9d9d9;
}
*{box-sizing:border-box;margin:0;padding:0}
html,body{width:1200px;height:804px;overflow:hidden}
body{font-family:"Lato",sans-serif;color:var(--text);background:var(--page);position:relative}
.abs{position:absolute}
.topbar{left:0;top:0;width:1200px;height:72px;background:var(--topbar);color:#fff}
.brand{left:24px;top:27px;display:flex;align-items:center;gap:6px;font-size:10px;font-weight:700}
.brand-dot{width:18px;height:18px;border-radius:50%;background:var(--brand)}
.divider{left:189px;top:4px;width:1px;height:64px;background:#555}
.page-title{left:208px;top:24px;font-size:17px}
.user{right:25px;top:24px;display:flex;align-items:center;gap:10px;font-size:17px}
.sidebar{left:0;top:72px;width:190px;height:732px;background:#fff}
.nav-item{position:absolute;left:0;width:189px;height:25px;display:flex;align-items:center;gap:6px;padding-left:9px;font-size:12px}
.nav-item.active{background:var(--nav-active);color:var(--accent)}
.nav-head{position:absolute;left:9px;font-size:12px}
.group{position:absolute;left:0;width:189px;height:24px;background:#ececec;display:flex;align-items:center;padding-left:8px;gap:8px;font-size:12px;box-shadow:0 2px 2px rgba(0,0,0,.08)}
.group-dot{width:15px;height:15px;border-radius:50%;background:#d4d4d4}
.caret{position:absolute;right:8px;top:9px;width:0;height:0;border-left:5px solid transparent;border-right:5px solid transparent}
.caret.up{border-bottom:6px solid #222}
.caret.down{border-top:6px solid #222}
.sub{position:absolute;left:33px;font-size:12px}
.collapse{left:161px;top:776px}
.label{font-size:12px}
.panel{background:var(--panel)}
.stat-box{border:1px solid var(--line);background:#fff;display:flex;align-items:center;justify-content:center;gap:12px;font-size:25px}
.btn{left:1081px;top:385px;width:102px;height:22px;background:var(--accent);color:#fff;font-size:10px;display:flex;align-items:center;justify-content:center}
.card{background:#fff;box-shadow:0 1px 5px rgba(0,0,0,.18);width:189px;height:206px;text-align:center}
.card h3{font-weight:400;font-size:17px;margin-top:3px}
.card .desc{font-size:9px;color:var(--muted);margin-top:2px}
.card .illus{width:81px;height:81px;border-radius:50%;background:var(--illus);margin:14px auto 0}
.card .count{display:flex;align-items:center;justify-content:center;gap:6px;margin-top:14px}
.card .num{font-size:27px;color:var(--accent);line-height:1}
.card .ct{text-align:left;font-size:9px;line-height:1.2}
.card .ct span{color:var(--muted);display:block}
.card .ct b{font-weight:700}
.card .since{font-size:9px;color:var(--muted);margin-top:14px}
.footer{left:190px;top:687px;width:1010px;height:117px;background:var(--topbar)}
</style>
</head>
<body>
<header class="abs topbar">
  <div class="abs brand"><span class="brand-dot"></span>PebbleLoom</div>
  <div class="abs divider"></div>
  <div class="abs page-title">Home</div>
  <div class="abs user">
    <svg width="21" height="21" viewBox="0 0 24 24" fill="none" stroke="#fff" stroke-width="1.5"><circle cx="12" cy="12" r="10.5"/><circle cx="12" cy="9" r="3.5"/><path d="M5.5 19c1.5-3 4-4 6.5-4s5 1 6.5 4"/></svg>
    Username
  </div>
</header>

<nav class="abs sidebar">
  <div class="nav-item active" style="top:0">
    <svg width="12" height="12" viewBox="0 0 24 24" fill="none" stroke="currentColor" stroke-width="2"><path d="M3 11l9-8 9 8v10h-6v-6H9v6H3z"/></svg>Home</div>
  <div class="nav-item" style="top:29px">
    <svg width="12" height="12" viewBox="0 0 24 24" fill="none" stroke="#aaa" stroke-width="2"><path d="M6 17V11a6 6 0 0112 0v6l2 2H4z"/></svg>All alerts</div>
  <div class="nav-item" style="top:58px">
    <svg width="12" height="12" viewBox="0 0 24 24" fill="none" stroke="#aaa" stroke-width="2"><circle cx="12" cy="12" r="9"/><circle cx="12" cy="12" r="3"/></svg>Manage</div>
  <div class="nav-head" style="top:100px">Campaigns</div>
  <div class="nav-head" style="top:100px;left:173px">+</div>
  <div class="group" style="top:127px"><span class="group-dot"></span>My custom campaign<span class="caret up"></span></div>
  <div class="sub" style="top:163px">Overview</div>
  <div class="sub" style="top:192px">Files &amp; HoneyTokens</div>
  <div class="sub" style="top:221px">Resources</div>
  <div class="sub" style="top:249px">Alerts</div>
  <div class="sub" style="top:278px">Settings</div>
  <div class="group" style="top:308px"><span class="group-dot"></span>Default campaign<span class="caret down"></span></div>
</nav>
<svg class="abs collapse" width="20" height="16" viewBox="0 0 20 16" fill="none" stroke="#111" stroke-width="2.5"><path d="M9 2L3 8l6 6M17 2l-6 6 6 6"/></svg>

<div class="abs label" style="left:208px;top:95px">Teamspace</div>
<section class="abs panel" style="left:207px;top:114px;width:976px;height:59px">
  <div style="position:absolute;left:14px;top:8px;font-size:20px">Default</div>
  <div style="position:absolute;left:15px;top:34px;font-size:9.5px;color:#555">The default client is created as a part of your user account.</div>
</section>

<div class="abs label" style="left:208px;top:193px">Subscription overview</div>
<section class="abs panel" style="left:207px;top:213px;width:478px;height:151px">
  <svg style="position:absolute;left:21px;top:18px" width="30" height="28" viewBox="0 0 30 28" fill="#111"><circle cx="3" cy="24" r="2.5"/><rect x="8" y="16" width="5" height="11" rx="2"/><rect x="15" y="10" width="5" height="17" rx="2"/><rect x="23" y="2" width="5" height="25" rx="2"/></svg>
  <div style="position:absolute;left:64px;top:25px;font-size:11.5px;color:var(--muted)">Your usage will show up here</div>
  <div style="position:absolute;left:20px;top:90px;font-size:11.5px">Starter pack usage</div>
  <div style="position:absolute;left:20px;top:107px;width:429px;height:2px;background:#9a9a9a"></div>
  <div style="position:absolute;left:20px;top:114px;font-size:9.5px;color:var(--muted)">0 files active out of 10 allowed</div>
</section>

<div class="abs label" style="left:709px;top:193px">Files &amp; Honey Tokens</div>
<section class="abs panel" style="left:708px;top:213px;width:475px;height:151px">
  <svg style="position:absolute;left:25px;top:15px" width="28" height="30" viewBox="0 0 28 30" fill="none" stroke="#111" stroke-width="2.2"><rect x="2" y="9" width="17" height="19" rx="2"/><path d="M8 9V3h17v19h-6M6 16h9M6 21h9"/></svg>
  <div style="position:absolute;left:67px;top:23px;font-size:12px;color:var(--muted)">Statistics</div>
</section>
<div class="abs stat-box" style="left:725px;top:291px;width:212px;height:58px">
  <svg width="22" height="22" viewBox="0 0 24 24" fill="none" stroke="#111" stroke-width="1.8"><path d="M21 11a9 9 0 11-4-7.5"/><path d="M7 11l4 4 10-10"/></svg>0</div>
<div class="abs stat-box" style="left:955px;top:291px;width:211px;height:58px">
  <svg width="22" height="24" viewBox="0 0 28 30" fill="none" stroke="#111" stroke-width="2.4"><rect x="2" y="9" width="17" height="19" rx="2"/><path d="M8 9V3h17v19h-6M6 16h9M6 21h9"/></svg>30</div>

<div class="abs label" style="left:208px;top:394px">Campaigns</div>
<div class="abs btn">New Campaign +</div>
<section class="abs panel" style="left:207px;top:412px;width:976px;height:253px"></section>

<article class="abs card" style="left:233px;top:436px">
  <h3>My custom campaign</h3>
  <div class="desc">This is my custom campaign for...</div>
  <div class="illus" role="img" aria-label="Grey circle illustration of gears and browser windows"></div>
  <div class="count"><span class="num">0</span><div class="ct"><span>Active</span><b>Files and HoneyTokens</b></div></div>
  <div class="since">Active since: Jul 25 2023 13:12</div>
</article>
<article class="abs card" style="left:450px;top:436px">
  <h3>Default campaign</h3>
  <div class="desc">Define your own mission, or...</div>
  <div class="illus" role="img" aria-label="Grey circle illustration of gears and browser windows"></div>
  <div class="count"><span class="num">0</span><div class="ct"><span>Active</span><b>Files and HoneyTokens</b></div></div>
  <div class="since">Active since: Jul 25 2023 13:12</div>
</article>

<footer class="abs footer" role="img" aria-label="Dark footer band with decorative hexagon pattern"></footer>
</body>
</html>
```